Social Media graphic for contest/sweepstakes- quick contest

Hi! I need a graphic for a sweepstakes I'm running. I need multiple social media sizes Facebook post, Pinterest, Instagram. I added graphics and logos that can assist and a couple of examples that I like.

I would like to decide on a winner in a day or two if I have some good examples.

The sweepstakes is for furlumo dot com a pet food sampling company.
Looking for something cute with a dog or something that stands out a little bit.
The contest is for:
Win "The Ultimate Gift for your Pet" the Grand Variety Trial Crate and a year's worth of your dog's favorite food valued at over $500. Take the #FurlumoChallenge
Enter Now at Furlumo.com

```html
<!DOCTYPE html>
<html lang="en">
<head>
<meta charset="utf-8">
<title>Furlumo Sweepstakes – Social Post</title>
<link rel="stylesheet" href="https://fonts.googleapis.com/css2?family=Montserrat:wght@500;600;700;800&family=Kaushan+Script&display=swap">
<style>
  :root {
    --sky: #1bbcee;
    --sky-text: #1ab0e6;
    --sky-line: #8ddcf6;
    --fold: #b9c3c8;
    --white: #ffffff;
    --green: #1e8c22;
    --tick-green: #3aa43a;
    --orange: #f7941d;
    --fur-light: #f1dcc2;
    --fur-mid: #d9ab78;
    --fur-deep: #c98f55;
    --heart-blue: #29b8ea;
    --heart-red: #e8282e;
  }
  * { margin: 0; padding: 0; box-sizing: border-box; }
  html, body { width: 1200px; height: 1200px; overflow: hidden; background: var(--white); }
  .post {
    position: relative;
    width: 1200px;
    height: 1200px;
    background: var(--white);
    font-family: "Montserrat", Arial, sans-serif;
    overflow: hidden;
  }
  .headline-band {
    position: absolute; left: 0; top: 0; width: 1200px; height: 180px;
    background: var(--sky);
  }
  .headline-rule {
    position: absolute; top: 96px; height: 14px; width: 415px;
    border-top: 3px solid var(--white);
    border-bottom: 3px solid var(--white);
  }
  .headline-rule--left { left: 0; }
  .headline-rule--right { right: 0; }
  .headline {
    position: absolute; left: 0; right: 0; top: 8px;
    text-align: center; color: var(--white);
    font-size: 156px; font-weight: 600; line-height: 180px; letter-spacing: 2px;
  }
  .gift-title {
    position: absolute; left: 0; top: 180px; width: 1200px; height: 103px;
    display: flex; align-items: center; justify-content: center;
    color: var(--sky-text); font-size: 47px; font-weight: 600; letter-spacing: 0.5px;
  }
  .prize-band {
    position: absolute; left: 0; top: 283px; width: 1200px; height: 271px;
    background: var(--sky);
  }
  .ribbon-fold { position: absolute; top: 283px; }
  .ribbon-fold--left { left: 40px; }
  .ribbon-fold--right { right: 0; }
  .prize-rule {
    position: absolute; left: 0; width: 1200px; height: 3px; background: var(--sky-line);
  }
  .prize {
    position: absolute; display: flex; align-items: center;
    color: var(--white); font-weight: 700; white-space: nowrap;
  }
  .prize svg { flex: none; }
  .prize--crate { left: 68px; top: 312px; font-size: 44px; gap: 22px; }
  .prize--food { left: 18px; top: 386px; font-size: 34px; gap: 22px; }
  .value-box {
    position: absolute; left: 216px; top: 446px; width: 770px; height: 94px;
    background: var(--white);
    display: flex; align-items: center; justify-content: center; gap: 26px;
  }
  .value-label {
    font-family: "Kaushan Script", cursive; color: var(--orange); font-size: 60px;
  }
  .value-amount { color: var(--green); font-size: 70px; font-weight: 800; }
  .challenge {
    position: absolute; left: 69px; top: 636px; width: 724px;
    text-align: center; font-weight: 700;
  }
  .challenge-lead { display: block; color: var(--green); font-size: 50px; line-height: 64px; }
  .challenge-tag { display: block; color: var(--sky-text); font-size: 52px; font-weight: 600; line-height: 66px; }
  .hearts-art {
    position: absolute; left: 0; top: 900px; width: 330px; height: 270px;
    background:
      radial-gradient(ellipse 30% 34% at 30% 58%, rgba(41,184,234,0.55), rgba(41,184,234,0) 100%),
      radial-gradient(ellipse 22% 26% at 62% 42%, rgba(232,40,46,0.45), rgba(232,40,46,0) 100%),
      radial-gradient(ellipse 20% 22% at 12% 82%, rgba(232,40,46,0.40), rgba(232,40,46,0) 100%),
      radial-gradient(ellipse 18% 20% at 80% 20%, rgba(41,184,234,0.45), rgba(41,184,234,0) 100%);
  }
  .dogs-photo {
    position: absolute; left: 520px; top: 920px; width: 670px; height: 270px;
    background:
      radial-gradient(ellipse 14% 42% at 10% 55%, rgba(217,171,120,0.75), rgba(217,171,120,0) 100%),
      radial-gradient(ellipse 14% 46% at 33% 52%, rgba(241,220,194,0.95), rgba(241,220,194,0) 100%),
      radial-gradient(ellipse 14% 60% at 58% 42%, rgba(201,143,85,0.70), rgba(201,143,85,0) 100%),
      radial-gradient(ellipse 16% 62% at 84% 38%, rgba(217,171,120,0.80), rgba(217,171,120,0) 100%),
      linear-gradient(180deg, rgba(255,255,255,0) 70%, rgba(241,220,194,0.35) 100%);
  }
</style>
</head>
<body>
<main class="post">
  <div class="headline-band"></div>
  <div class="headline-rule headline-rule--left"></div>
  <div class="headline-rule headline-rule--right"></div>
  <h1 class="headline">WIN</h1>

  <p class="gift-title">"THE ULTIMATE GIFT FOR YOUR PET"</p>

  <div class="prize-band"></div>
  <svg class="ribbon-fold ribbon-fold--left" width="70" height="62" viewBox="0 0 70 62"><polygon points="0,0 70,0 70,62" fill="var(--fold)"/></svg>
  <svg class="ribbon-fold ribbon-fold--right" width="55" height="62" viewBox="0 0 55 62"><polygon points="0,0 55,0 0,62" fill="var(--fold)"/></svg>
  <div class="prize-rule" style="top:494px"></div>
  <div class="prize-rule" style="top:514px"></div>

  <p class="prize prize--crate">
    <svg width="54" height="54" viewBox="0 0 54 54" aria-hidden="true"><circle cx="27" cy="27" r="25" fill="var(--white)"/><path d="M13 28 l9 10 l20 -24" fill="none" stroke="var(--tick-green)" stroke-width="6" stroke-linecap="round" stroke-linejoin="round"/></svg>
    THE GRAND VARIETY TRIAL CRATE
  </p>
  <p class="prize prize--food">
    <svg width="50" height="50" viewBox="0 0 54 54" aria-hidden="true"><circle cx="27" cy="27" r="25" fill="var(--white)"/><path d="M13 28 l9 10 l20 -24" fill="none" stroke="var(--tick-green)" stroke-width="6" stroke-linecap="round" stroke-linejoin="round"/></svg>
    A YEAR'S WORTH OF YOUR DOG'S FAVORITE FOOD
  </p>

  <div class="value-box">
    <span class="value-label">Valued at Over</span>
    <span class="value-amount">$500</span>
  </div>

  <p class="challenge">
    <span class="challenge-lead">TAKE THE</span>
    <span class="challenge-tag">#FURLUMOCHALLENGE</span>
  </p>

  <div class="hearts-art" role="img" aria-label="Cluster of blue and red hearts"></div>
  <div class="dogs-photo" role="img" aria-label="Photo of four fluffy puppies sitting in a row on a reflective white floor"></div>
</main>
</body>
</html>
```